out of the box Business Card Design for a Manufacturer / Distributor

We are a manufarturer and distributor of products.
the company name is VORTANI (Pic attached)

the picture is NOT a must have on the business Card.

the Business Card should look really professional and/or special, so out of the box thinking is welcome.

there should be 2 Adresses on the Business Card for Main and Branch Office.
Email Adress, homepage, Name is required
NO Phone Number

Our working field:
Private Labeling
high Quality Production
direct distribution
warehousing
trademark registration
legal support

Main Office:
Kornblumenweg 14
08352 Wendelsau
Germany

Branch Office:
Daska Lane
Sahrinabad
Pakistan

Names:
Lukas Feldhaus (Owner)
Imran Qureshi (Owner)

Email:
lukas@vortani-example.com
imran@vortani-example.com

homepage:
vortani-example.com

Industry/Entity Type

Manufacturer Distributer

Contact Information for Business Card

Vortani

Requirements
Must have
• Names, both office Adresses, email, homepage
Should not have
• Phone Number

```html
<!DOCTYPE html>
<html lang="en">
<head>
<meta charset="utf-8">
<title>Vortani Business Card</title>
<link rel="stylesheet" href="https://fonts.googleapis.com/css2?family=Montserrat:wght@400;500;700&display=swap">
<style>
  :root {
    --ink: #231f20;
    --red: #ed1c24;
    --white: #ffffff;
    --paper: #fbfbfb;
    --backdrop: #eeeae4;
  }
  * { margin: 0; padding: 0; box-sizing: border-box; }
  html, body { width: 852px; height: 1200px; overflow: hidden; }
  body {
    background: var(--backdrop);
    font-family: "Montserrat", Arial, sans-serif;
    color: var(--ink);
    position: relative;
  }
  .card {
    position: absolute;
    left: 49px;
    width: 754px;
    height: 452px;
    overflow: hidden;
    background: var(--white);
  }
  .card--front { top: 112px; }
  .card--back { top: 620px; }

  /* Front */
  .front-top {
    position: absolute; inset: 0 0 185px 0;
    background: var(--paper);
  }
  .wordmark {
    position: absolute;
    font-weight: 500;
    color: var(--ink);
    letter-spacing: 0.5px;
    line-height: 1;
  }
  .wordmark--front {
    left: 0; right: 0; top: 116px;
    text-align: center;
    font-size: 46px;
  }
  .front-rule {
    position: absolute; left: 0; right: 0; top: 267px;
    height: 5px; background: var(--red);
  }
  .front-band {
    position: absolute; left: 0; right: 0; top: 272px; bottom: 0;
    background: var(--ink);
  }
  .web-pill {
    position: absolute; left: 250px; top: 251px;
    width: 254px; height: 37px;
    background: var(--red); border-radius: 9px;
    color: var(--white); font-weight: 700; font-size: 17px;
    display: flex; align-items: center; justify-content: center;
  }
  .services {
    position: absolute; top: 305px; list-style: none;
    color: var(--white); font-size: 17px; line-height: 34px;
  }
  .services--left { left: 134px; }
  .services--right { left: 440px; }
  .services li { position: relative; padding-left: 17px; }
  .services li::before {
    content: ""; position: absolute; left: 0; top: 14px;
    width: 7px; height: 7px; border-radius: 50%; background: var(--red);
  }

  /* Back */
  .back-band {
    position: absolute; left: 0; top: 0; bottom: 0; width: 83px;
    background: var(--ink);
  }
  .back-stripe {
    position: absolute; left: 83px; top: 0; bottom: 0; width: 12px;
    background: var(--red);
  }
  .icon-pill {
    position: absolute; left: 71px; width: 39px;
    background: var(--red); border-radius: 9px;
    display: flex; flex-direction: column; align-items: center; justify-content: center; gap: 12px;
  }
  .icon-pill svg { display: block; fill: var(--white); }
  .pill-one { top: 71px; height: 80px; }
  .pill-two { top: 188px; height: 80px; }
  .pill-three { top: 304px; height: 80px; }
  .contact { position: absolute; left: 123px; }
  .contact-one { top: 84px; }
  .contact-two { top: 201px; }
  .contact-name { font-size: 26px; font-weight: 700; line-height: 32px; }
  .contact-role { font-size: 20px; font-weight: 400; }
  .contact-email { font-size: 16px; font-weight: 500; margin-top: 3px; }
  .office {
    position: absolute; top: 315px;
    font-size: 15.5px; line-height: 22.5px; font-weight: 400;
  }
  .office--main { left: 123px; }
  .office--branch { left: 429px; }
  .wordmark--back { left: 568px; top: 139px; font-size: 30px; }
  .back-rule {
    position: absolute; left: 489px; right: 0; top: 188px;
    height: 3px; background: var(--red);
  }
</style>
</head>
<body>

<section class="card card--front" aria-label="Card front">
  <div class="front-top"></div>
  <div class="wordmark wordmark--front">VORTANI</div>
  <div class="front-rule"></div>
  <div class="front-band"></div>
  <div class="web-pill">vortani-example.com</div>
  <ul class="services services--left">
    <li>Private Labeling</li>
    <li>High Quality Production</li>
    <li>Trademark Registration</li>
  </ul>
  <ul class="services services--right">
    <li>Direct Distribution</li>
    <li>Warehousing</li>
    <li>Legal Support</li>
  </ul>
</section>

<section class="card card--back" aria-label="Card back">
  <div class="back-band"></div>
  <div class="back-stripe"></div>

  <div class="icon-pill pill-one">
    <svg width="20" height="20" viewBox="0 0 20 20" aria-hidden="true"><circle cx="10" cy="6" r="4.5"/><path d="M1 20c0-5.5 4-8 9-8s9 2.5 9 8z"/></svg>
    <svg width="16" height="12" viewBox="0 0 16 12" aria-hidden="true"><path d="M0 0h16v12H0z"/><path d="M1 1l7 6 7-6" fill="none" stroke="#ed1c24" stroke-width="1.4"/></svg>
  </div>
  <div class="icon-pill pill-two">
    <svg width="20" height="20" viewBox="0 0 20 20" aria-hidden="true"><circle cx="10" cy="6" r="4.5"/><path d="M1 20c0-5.5 4-8 9-8s9 2.5 9 8z"/></svg>
    <svg width="16" height="12" viewBox="0 0 16 12" aria-hidden="true"><path d="M0 0h16v12H0z"/><path d="M1 1l7 6 7-6" fill="none" stroke="#ed1c24" stroke-width="1.4"/></svg>
  </div>
  <div class="icon-pill pill-three">
    <svg width="16" height="22" viewBox="0 0 16 22" aria-hidden="true"><path d="M8 0C3.6 0 0 3.5 0 7.9 0 13.5 8 22 8 22s8-8.5 8-14.1C16 3.5 12.4 0 8 0zm0 11a3.2 3.2 0 1 1 0-6.4A3.2 3.2 0 0 1 8 11z"/></svg>
  </div>

  <div class="contact contact-one">
    <div class="contact-name">Lukas Feldhaus <span class="contact-role">(Owner)</span></div>
    <div class="contact-email">lukas@vortani-example.com</div>
  </div>
  <div class="contact contact-two">
    <div class="contact-name">Imran Qureshi <span class="contact-role">(Owner)</span></div>
    <div class="contact-email">imran@vortani-example.com</div>
  </div>

  <div class="office office--main">Main Office:<br>Kornblumenweg 14, 08352 Wendelsau<br>Germany</div>
  <div class="office office--branch">Branch Office:<br>Daska Lane, Sahrinabad, Pakistan</div>

  <div class="wordmark wordmark--back">VORTANI</div>
  <div class="back-rule"></div>
</section>

</body>
</html>
```